Oregon Pawnbroker About Us Brochure

We need to make a front/back tri-fold "about us" informative brochure using the bullet points uploaded. Our association represents licensed pawnbrokers in the state of Oregon and this will be distributed to the entire legislative body in our state. I have attached our logo, but feel free to be creative with logo to enhance the overall appearance of the brochure.

Target Market(s)

Regulators and Politicians

Industry/Entity Type

Pawnbroker

Requirements
Must have
• Professional Appearance
Nice to have
• Graphics, color scheme

```html
<!DOCTYPE html>
<html lang="en">
<head>
<meta charset="utf-8">
<title>Quick Facts about Oregon Pawnbrokers – Tri-fold Brochure</title>
<link href="https://fonts.googleapis.com/css2?family=Bree+Serif&family=PT+Sans:wght@400;700&display=swap" rel="stylesheet">
<style>
  :root {
    --navy: #2b2a7c;
    --navy-soft: #3a3990;
    --orange: #ef6b23;
    --yellow: #f2c21b;
    --lavender: #e7e5f4;
    --ink: #23224f;
    --white: #ffffff;
    --stage: #ecebe7;
    --sky-top: #5f8fd6;
    --sky-low: #c9dbf2;
    --photo-grey: #d9dbe0;
    --photo-warm: #b9a593;
  }
  * { box-sizing: border-box; margin: 0; padding: 0; }
  html, body { width: 1200px; height: 927px; overflow: hidden; }
  body {
    background: var(--stage);
    font-family: "PT Sans", Arial, sans-serif;
    color: var(--ink);
    position: relative;
  }
  .spread {
    position: absolute;
    top: 237px;
    width: 585px;
    height: 452px;
    display: flex;
    background: var(--white);
    box-shadow: 0 6px 18px rgba(0,0,0,.18);
    overflow: hidden;
  }
  .spread--inside { left: 10px; }
  .spread--outside { left: 605px; }
  .panel {
    position: relative;
    width: 195px;
    height: 100%;
    overflow: hidden;
  }
  .panel + .panel { border-left: 1px solid rgba(0,0,0,.06); }

  /* inside spread */
  .panel-header {
    height: 96px;
    background: var(--navy);
    display: flex;
    flex-direction: column;
    justify-content: flex-end;
    align-items: center;
    padding: 0 12px 14px;
    text-align: center;
  }
  .panel-title {
    font-family: "Bree Serif", Georgia, serif;
    color: var(--orange);
    font-size: 19px;
    line-height: 1.05;
  }
  .panel-subtitle {
    color: var(--orange);
    font-size: 13px;
    margin-top: 2px;
  }
  .panel-body { padding: 12px 12px 0 12px; }
  .panel--lavender { background: var(--lavender); }
  .fact-list { list-style: none; }
  .fact-list li {
    position: relative;
    padding-left: 12px;
    font-size: 9.6px;
    line-height: 1.28;
    margin-bottom: 6px;
  }
  .fact-list li::before {
    content: "";
    position: absolute;
    left: 1px; top: 4px;
    width: 5px; height: 5px;
    border-radius: 50%;
    background: var(--orange);
  }
  .sub-list { list-style: none; margin-top: 3px; }
  .sub-list li { margin-bottom: 2px; }
  .sub-list li::before { border-radius: 0; background: var(--ink); width: 4px; height: 4px; }
  .base-band {
    position: absolute;
    left: 0; right: 0; bottom: 0;
    height: 22px;
    background: var(--orange);
    color: var(--white);
    font-size: 8px;
    display: flex;
    align-items: center;
    justify-content: flex-end;
    padding-right: 10px;
  }
  .laptop-photo {
    position: absolute;
    left: 0; right: 0; bottom: 22px;
    height: 190px;
    background: linear-gradient(160deg, var(--white) 0%, var(--photo-grey) 45%, var(--photo-warm) 100%);
  }

  /* outside spread */
  .consumer-panel { padding: 26px 14px 0 14px; }
  .consumer-panel .panel-title { text-align: center; font-size: 17px; margin-bottom: 14px; }
  .consumer-panel .fact-list li { font-size: 10px; margin-bottom: 8px; }

  .association-panel { background: var(--navy); color: var(--white); }
  .association-panel .curve { position: absolute; left: 0; bottom: 0; width: 195px; height: 170px; }
  .association-panel .panel-title { text-align: center; padding: 28px 12px 14px; font-size: 17px; }
  .association-panel .fact-list { padding: 0 14px 0 18px; position: relative; }
  .association-panel .fact-list li { font-size: 10.2px; margin-bottom: 8px; }
  .association-panel .fact-list li::before { background: var(--white); }

  .seal {
    display: flex;
    align-items: center;
    gap: 6px;
    font-family: "PT Sans", Arial, sans-serif;
    font-weight: 700;
    font-size: 9px;
    line-height: 1.1;
    color: var(--navy);
  }
  .seal-dot {
    flex: none;
    width: 30px; height: 30px;
    border-radius: 50%;
    background: var(--white);
    border: 2px solid var(--orange);
  }
  .association-panel .seal {
    position: absolute;
    left: 34px; bottom: 64px;
    background: var(--white);
    padding: 6px 8px 6px 6px;
    border-radius: 22px;
  }
  .site-url {
    position: absolute;
    left: 0; right: 0; bottom: 12px;
    text-align: center;
    font-size: 8px;
    font-weight: 700;
    color: var(--white);
  }

  .cover-panel { background: var(--white); }
  .cover-title {
    position: absolute;
    left: 22px; top: 26px;
    font-family: "Bree Serif", Georgia, serif;
    color: var(--orange);
    font-size: 42px;
    line-height: .9;
  }
  .cover-title .indent { display: block; padding-left: 36px; }
  .chat-icon { position: absolute; left: 20px; top: 70px; width: 30px; height: 24px; }
  .cover-sub {
    position: absolute;
    left: 20px; top: 118px;
    font-size: 10.5px;
    color: var(--navy);
  }
  .cover-sub strong { font-weight: 700; }
  .cover-panel .seal { position: absolute; right: 14px; top: 140px; }
  .city-photo {
    position: absolute;
    left: 0; right: 0; bottom: 0;
    height: 250px;
    background: linear-gradient(180deg, var(--sky-top) 0%, var(--sky-low) 60%, var(--navy-soft) 100%);
  }
  .cover-wave { position: absolute; left: 0; bottom: 0; width: 195px; height: 60px; }
</style>
</head>
<body>

<section class="spread spread--inside" aria-label="Brochure inside">
  <article class="panel">
    <header class="panel-header"><h2 class="panel-title">About Our<br>Industry</h2></header>
    <div class="panel-body">
      <ul class="fact-list">
        <li>Pawnbroking is the oldest form of regulated consumer credit.</li>
        <li>The Department of Consumer and Business Services issues the pawnbroker licenses here in Oregon.</li>
        <li>Currently, Oregon has 83 individually licensed pawnshops, 78 of which are brick-and-mortar, family-owned and operated businesses.</li>
        <li>Pawnbrokers offer highly regulated safety-net funds to consumers on a face-to-face basis from Main Street locations across the state.</li>
        <li>Lending decisions are solely based on the collateral and pawn transactions are non-recourse. No credit inquiries, No credit reporting, No collections, No cycle of debt.</li>
        <li>Pawnbrokers provide safe, secure storage for items customers cannot or do not want to store themselves, including oversized or seasonal items construction equipment, and firearms.</li>
      </ul>
    </div>
    <div class="base-band"></div>
  </article>

  <article class="panel panel--lavender">
    <header class="panel-header"><h2 class="panel-title">Regulation</h2></header>
    <div class="panel-body">
      <ul class="fact-list">
        <li>Pawnshops are heavily regulated and work closely with the federal, state and local governments and law enforcement.</li>
        <li>ORS 726 and OAR 441-740 define the requirements for our industry here in Oregon including the requirements of a loan, duration of a loan, as well as the interest and fees charged.</li>
        <li>Transactions require customer to present government issued photo identification.</li>
        <li>All transactions are reported daily to law enforcement.</li>
        <li>Oregon Pawnbrokers work closely with the following regulators:
          <ul class="sub-list fact-list">
            <li>Department of Consumer and Business Services</li>
            <li>Bureau of Alcohol Tobacco and Firearms</li>
            <li>State Police</li>
            <li>Department of Agriculture</li>
          </ul>
        </li>
      </ul>
    </div>
    <div class="base-band"></div>
  </article>

  <article class="panel">
    <header class="panel-header">
      <h2 class="panel-title">Oregon Pawnbroker<br>Statistics</h2>
      <p class="panel-subtitle">(as reported by DCBS)</p>
    </header>
    <div class="panel-body">
      <ul class="fact-list">
        <li>Average loan amount in 2020 was $175</li>
        <li>Redemption rate of 72%</li>
        <li>Oregon pawnshops made approximately 206,500 loans in 2020, lending $33.2 million to Oregon customers.</li>
        <li>Police pickup rate of 0.085%</li>
      </ul>
    </div>
    <div class="laptop-photo" role="img" aria-label="Photo of a hand holding a payment card over a laptop keyboard"></div>
    <div class="base-band">www.cascadepawnalliance.org</div>
  </article>
</section>

<section class="spread spread--outside" aria-label="Brochure outside">
  <article class="panel consumer-panel">
    <h2 class="panel-title">Why Pawnbrokers are Important to Oregon Consumers</h2>
    <ul class="fact-list">
      <li>Without state-licensed pawnbrokers, Oregonians could be forced to borrow from unlicensed people with unregulated loans that include very high interest rates or instead, forced to sell their property entirely, diminishing their personal assets.</li>
      <li>Other credit based lenders, such as banks and credit unions, do not offer Oregonians loan products at the small dollar amounts our industry serves.</li>
      <li>Pawnbrokers provide a same day financial solution.</li>
      <li>Pawnbrokers are invested in our communities and are sensitive to the needs of our customers.</li>
    </ul>
  </article>

  <article class="panel association-panel">
    <svg class="curve" viewBox="0 0 195 170" preserveAspectRatio="none" aria-hidden="true">
      <defs>
        <linearGradient id="warmCurve" x1="0" y1="0" x2="1" y2="0">
          <stop offset="0" stop-color="#ef6b23"/>
          <stop offset="1" stop-color="#f2c21b"/>
        </linearGradient>
      </defs>
      <path d="M0 40 Q100 95 195 20 L195 170 L0 170 Z" fill="url(#warmCurve)"/>
    </svg>
    <h2 class="panel-title">About the Cascade Pawnbroker Alliance</h2>
    <ul class="fact-list">
      <li>United voice of Oregon Pawnbrokers</li>
      <li>Represents majority of pawnbrokers, both number of licensees and transactions processed</li>
      <li>Single point of contact for Oregon Legislature and all regulators to communicate with our industry.</li>
    </ul>
    <div class="seal"><span class="seal-dot"></span><span>Cascade Pawnbroker<br>Alliance</span></div>
    <p class="site-url">www.cascadepawnalliance.org</p>
  </article>

  <article class="panel cover-panel">
    <h1 class="cover-title">Quick<span class="indent">Facts</span></h1>
    <svg class="chat-icon" viewBox="0 0 30 24" aria-hidden="true">
      <ellipse cx="12" cy="10" rx="10" ry="8" fill="#fff" stroke="#23224f" stroke-width="1.6"/>
      <path d="M6 16 L4 22 L11 17" fill="#fff" stroke="#23224f" stroke-width="1.6"/>
      <text x="12" y="14" font-size="11" font-weight="700" text-anchor="middle" fill="#23224f" font-family="PT Sans, sans-serif">?</text>
    </svg>
    <p class="cover-sub">about <strong>Oregon Pawnbrokers</strong></p>
    <div class="seal"><span class="seal-dot"></span><span>Cascade Pawnbroker<br>Alliance</span></div>
    <div class="city-photo" role="img" aria-label="Photo of glass office towers against a blue sky"></div>
    <svg class="cover-wave" viewBox="0 0 195 60" preserveAspectRatio="none" aria-hidden="true">
      <path d="M0 60 L0 40 Q90 10 195 0 L195 60 Z" fill="#fff"/>
    </svg>
  </article>
</section>

</body>
</html>
```